Resinex Pro color chart design

We are in need to have a color chart (pdf to be displayed on our website-www.resinexpro-sample.com as well as for print) to show customers what their color choices are for our metallic epoxy pigments. We would like it to be modern amd clean. A white background will allow the color swatches to stand out. our company colors are orange, grey and white. Looking for the color swatches to be as large as possible while still being able to display our logo, contact info and disclaimers. We are open to any design ideas. If needed it can be put on two pages.

Additional info to add: Resinex Pro Shimmer Tint Powders are special effect pigments composed of mica nano-particles coated with various organic and inorganic pigments to create pearlescent and iridescent effects that mimic the
natural look of stone and rock formations. These unique pigments are designed to be field blended with Resinex Pro Artisan Lustre clear epoxy. When the metallic particles are mixed with our epoxy they give the coating a shine that reflects light and creates an eye-catching dramatic color. For the most vivid color and dynamic effects we recommend (1) 16oz jar of metallic pigment for each 3 Gallon kit of our Artisan Lustre Epoxy.

Disclaimer: The colors on this chart are represented as closely as possible. Variations should be expected due to differences in substrate conditions, thickness of application, speed of curing, blending of colors, application technique, color of initial primer coat and screen resolution. For additional information and application instructions visit www.resinexpro-sample.com

Contact info: Tel. 1-800-555-0147
www.resinexpro-sample.com

Target Market(s)

Online. This will be a link on our website

Font styles to use
Sans Serif

Colors
f37122
5c5c5c
ffffff

Requirements
Must have
• A white background will allow the color swatches to stand out. Disclaimer should be in small print but still readable.
Nice to have
• Can use our company colors as part of the design
Should not have
• Should not look and feel cluttered.

```html
<!DOCTYPE html>
<html lang="en">
<head>
<meta charset="utf-8">
<title>Resinex Pro Color Chart</title>
<link rel="stylesheet" href="https://fonts.googleapis.com/css2?family=Open+Sans:wght@400;600;700;800&display=swap">
<style>
  :root {
    --orange: #f37122;
    --grey: #5c5c5c;
    --grey-light: #e6e6e6;
    --white: #ffffff;
  }
  * { margin: 0; padding: 0; box-sizing: border-box; }
  html, body { width: 707px; height: 1200px; overflow: hidden; background: var(--white); }
  body { font-family: "Open Sans", Arial, sans-serif; color: var(--grey); }
  .chart { position: relative; width: 707px; height: 1200px; background: var(--white); overflow: hidden; }

  .header { position: absolute; left: 0; top: 0; width: 707px; height: 430px; }
  .header svg { position: absolute; left: 0; top: 0; }

  .brand { position: absolute; left: 400px; top: 62px; width: 290px; }
  .brand-name { display: flex; align-items: center; gap: 10px; font-size: 32px; font-weight: 800; color: var(--orange); letter-spacing: -0.5px; line-height: 1; white-space: nowrap; }
  .brand-dot { width: 30px; height: 30px; border-radius: 50%; background: var(--orange); flex: none; }
  .brand-tagline { margin-top: 6px; margin-left: 40px; font-size: 10px; color: var(--grey); white-space: nowrap; }

  .phone-pill { position: absolute; right: 0; top: 392px; background: var(--orange); color: var(--white); font-weight: 700; font-size: 16px; padding: 7px 22px 7px 26px; border-radius: 20px 0 0 20px; }

  .swatches { position: absolute; left: 38px; top: 448px; width: 631px; display: grid; grid-template-columns: repeat(8, 1fr); column-gap: 11px; row-gap: 18px; }
  .swatch { text-align: center; }
  .swatch-chip { height: 100px; border-radius: 2px; background: linear-gradient(135deg, var(--c2) 0%, var(--c) 45%, var(--c2) 100%); box-shadow: 0 1px 3px rgba(0,0,0,0.25); }
  .swatch-name { margin-top: 6px; font-size: 8.5px; font-weight: 700; color: var(--grey); letter-spacing: 0.2px; white-space: nowrap; }

  .info-tab { position: absolute; left: 0; top: 876px; width: 707px; height: 30px; }
  .info-tab .bar { position: absolute; left: 0; top: 0; width: 420px; height: 30px; background: var(--orange); border-radius: 0 15px 15px 0; }
  .info-tab h2 { position: absolute; left: 40px; top: 5px; font-size: 15px; font-weight: 700; color: var(--white); }

  .info { position: absolute; left: 40px; top: 916px; width: 627px; font-size: 11px; line-height: 1.45; }
  .info p + p { margin-top: 5px; }
  .info .recommend { color: var(--orange); font-weight: 600; }

  .disclaimer { position: absolute; left: 40px; top: 1076px; width: 627px; }
  .disclaimer h3 { font-size: 14px; font-weight: 700; color: var(--orange); margin-bottom: 3px; }
  .disclaimer p { font-size: 8.5px; line-height: 1.45; }

  .footer { position: absolute; left: 0; top: 1150px; width: 707px; height: 50px; }
  .footer-line { position: absolute; left: 40px; right: 40px; top: 0; height: 1px; background: var(--grey-light); }
  .footer-note { position: absolute; left: 40px; top: 11px; font-size: 9px; color: var(--grey); }
  .footer-url { position: absolute; left: 260px; top: 9px; font-size: 11px; font-weight: 600; color: var(--orange); }
  .footer-phone { position: absolute; right: 40px; top: 5px; font-size: 18px; font-weight: 800; color: var(--orange); }
  .footer-band { position: absolute; left: 0; bottom: 0; width: 707px; height: 10px; background: var(--orange); }
</style>
</head>
<body>
<main class="chart">

  <header class="header">
    <svg width="707" height="430" viewBox="0 0 707 430">
      <defs>
        <radialGradient id="cans" cx="50%" cy="45%" r="60%">
          <stop offset="0" stop-color="#f5d21c"/>
          <stop offset="0.35" stop-color="#e8462a"/>
          <stop offset="0.6" stop-color="#2a7fd4"/>
          <stop offset="0.85" stop-color="#3aa64a"/>
          <stop offset="1" stop-color="#9a9a9a"/>
        </radialGradient>
        <linearGradient id="floor" x1="0" y1="0" x2="0" y2="1">
          <stop offset="0" stop-color="#3a3a3a"/>
          <stop offset="0.5" stop-color="#6b4a3a"/>
          <stop offset="1" stop-color="#c4552a"/>
        </linearGradient>
      </defs>
      <path d="M -20 58 Q 300 -30 707 18 L 707 36 Q 300 -8 -20 86 Z" fill="var(--orange)"/>
      <path d="M 0 360 Q 160 420 330 330 Q 420 280 707 300 L 707 318 Q 430 300 340 350 Q 160 440 0 382 Z" fill="var(--orange)"/>
      <path d="M 300 392 Q 500 370 707 380" stroke="var(--grey-light)" stroke-width="3" fill="none"/>
      <circle cx="160" cy="205" r="162" fill="var(--white)"/>
      <circle cx="160" cy="205" r="158" fill="none" stroke="var(--orange)" stroke-width="8"/>
      <circle cx="160" cy="205" r="148" fill="url(#cans)" role="img" aria-label="Photo of open paint cans filled with bright colors"/>
      <circle cx="530" cy="265" r="112" fill="var(--white)"/>
      <circle cx="530" cy="265" r="108" fill="none" stroke="var(--orange)" stroke-width="7"/>
      <circle cx="530" cy="265" r="100" fill="url(#floor)" role="img" aria-label="Photo of a room with a glossy metallic epoxy floor"/>
    </svg>

    <div class="brand">
      <div class="brand-name"><span class="brand-dot"></span>resinexpro</div>
      <div class="brand-tagline">Premium metallic epoxy floor systems</div>
    </div>

    <div class="phone-pill">1-800-555-0147</div>
  </header>

  <section class="swatches" aria-label="Color swatches">
    <div class="swatch"><div class="swatch-chip" style="--c:#d6317a;--c2:#f07ab0"></div><div class="swatch-name">BUBBLEGUM</div></div>
    <div class="swatch"><div class="swatch-chip" style="--c:#e2561e;--c2:#f39a5a"></div><div class="swatch-name">TANGERINE</div></div>
    <div class="swatch"><div class="swatch-chip" style="--c:#d98a1c;--c2:#f2c35a"></div><div class="swatch-name">ORANGE GOLD</div></div>
    <div class="swatch"><div class="swatch-chip" style="--c:#a9541f;--c2:#d98c56"></div><div class="swatch-name">COPPER</div></div>
    <div class="swatch"><div class="swatch-chip" style="--c:#8a3c1e;--c2:#bd6a45"></div><div class="swatch-name">CINNAMON</div></div>
    <div class="swatch"><div class="swatch-chip" style="--c:#7a1224;--c2:#b03348"></div><div class="swatch-name">WINE RED</div></div>
    <div class="swatch"><div class="swatch-chip" style="--c:#9c4a2a;--c2:#cf7d55"></div><div class="swatch-name">PENNY</div></div>
    <div class="swatch"><div class="swatch-chip" style="--c:#a67c2e;--c2:#d9b66a"></div><div class="swatch-name">BRASS</div></div>

    <div class="swatch"><div class="swatch-chip" style="--c:#e3b81c;--c2:#f7df6a"></div><div class="swatch-name">CANARY</div></div>
    <div class="swatch"><div class="swatch-chip" style="--c:#6d6a2a;--c2:#a09c55"></div><div class="swatch-name">CAMO</div></div>
    <div class="swatch"><div class="swatch-chip" style="--c:#a39a22;--c2:#d3cb5e"></div><div class="swatch-name">OLIVE YELLOW</div></div>
    <div class="swatch"><div class="swatch-chip" style="--c:#16867a;--c2:#4fc2b3"></div><div class="swatch-name">SEA GREEN</div></div>
    <div class="swatch"><div class="swatch-chip" style="--c:#1f5e32;--c2:#4e9462"></div><div class="swatch-name">FOREST GREEN</div></div>
    <div class="swatch"><div class="swatch-chip" style="--c:#4ea62c;--c2:#8fd463"></div><div class="swatch-name">GREEN APPLE</div></div>
    <div class="swatch"><div class="swatch-chip" style="--c:#4a3122;--c2:#7d5a44"></div><div class="swatch-name">COFFEE</div></div>
    <div class="swatch"><div class="swatch-chip" style="--c:#3f4448;--c2:#777d82"></div><div class="swatch-name">GUNMETAL</div></div>

    <div class="swatch"><div class="swatch-chip" style="--c:#e6ded2;--c2:#f9f6f0"></div><div class="swatch-name">PEARL</div></div>
    <div class="swatch"><div class="swatch-chip" style="--c:#d7dbe0;--c2:#f6f8fa"></div><div class="swatch-name">DIAMOND</div></div>
    <div class="swatch"><div class="swatch-chip" style="--c:#a9adb1;--c2:#dcdfe2"></div><div class="swatch-name">SILVER</div></div>
    <div class="swatch"><div class="swatch-chip" style="--c:#7b7f83;--c2:#b2b6ba"></div><div class="swatch-name">TITANIUM</div></div>
    <div class="swatch"><div class="swatch-chip" style="--c:#3f93d1;--c2:#86c3ec"></div><div class="swatch-name">SKY BLUE</div></div>
    <div class="swatch"><div class="swatch-chip" style="--c:#1b4f94;--c2:#4f82c4"></div><div class="swatch-name">OCEAN BLUE</div></div>
    <div class="swatch"><div class="swatch-chip" style="--c:#9c86c4;--c2:#cfc0e6"></div><div class="swatch-name">LILAC</div></div>
    <div class="swatch"><div class="swatch-chip" style="--c:#4e2a72;--c2:#7e58a6"></div><div class="swatch-name">GRAPE</div></div>
  </section>

  <div class="info-tab"><div class="bar"></div><h2>Additional Info To Add</h2></div>

  <section class="info">
    <p>Resinex Pro Shimmer Tint Powders are special effect pigments composed of mica nano-particles coated with various organic and inorganic pigments to create pearlescent and iridescent effects that mimic the natural look of stone and rock formations.</p>
    <p>These unique pigments are designed to be field blended with Resinex Pro Artisan Lustre clear epoxy. When the metallic particles are mixed with our epoxy they give the coating a shine that reflects light and creates an eye-catching dramatic color.</p>
    <p class="recommend">For the most vivid color and dynamic effects we recommend (1) 16oz jar of metallic pigment for each 3 Gallon kit of our Artisan Lustre Epoxy.</p>
  </section>

  <section class="disclaimer">
    <h3>Disclaimer</h3>
    <p>The colors on this chart are represented as closely as possible. Variations should be expected due to differences in substrate conditions, thickness of application, speed of curing, blending of colors, application technique, color of initial primer coat and screen resolution. For additional information and application instructions visit www.resinexpro-sample.com</p>
  </section>

  <footer class="footer">
    <div class="footer-line"></div>
    <div class="footer-note">Metallic epoxy pigment color chart</div>
    <div class="footer-url">www.resinexpro-sample.com</div>
    <div class="footer-phone">1-800-555-0147</div>
    <div class="footer-band"></div>
  </footer>

</main>
</body>
</html>
```